Professional Report Cover

We need a cover for CFO report (the document is about 20 pages, in case you decide to provide 3D mockup). The design must be professional. The main color has to be #299FC0, which can be incorporated with white, #375172, and #E3E7EE. See attached for content and logo.

```html
<!DOCTYPE html>
<html lang="en">
<head>
<meta charset="utf-8">
<title>The CFO Insight – Report Cover</title>
<link href="https://fonts.googleapis.com/css2?family=Barlow:wght@300;400;500&family=Montserrat:wght@600&display=swap" rel="stylesheet">
<style>
  :root {
    --navy: #07344f;
    --ink: #375172;
    --teal: #299FC0;
    --mist: #E3E7EE;
    --white: #ffffff;
    --grey: #5b6470;
  }
  html, body {
    margin: 0;
    padding: 0;
    width: 800px;
    height: 1200px;
    overflow: hidden;
    background: var(--navy);
  }
  .cover {
    position: relative;
    width: 800px;
    height: 1200px;
    background: var(--navy);
    font-family: "Barlow", Arial, sans-serif;
    color: var(--white);
    overflow: hidden;
  }
  .title {
    position: absolute;
    left: 60px;
    top: 96px;
    margin: 0;
    font-weight: 500;
    font-size: 196px;
    line-height: 184px;
    letter-spacing: 0;
    color: var(--mist);
  }
  .title span { display: block; }
  .title .line-cfo { margin-left: 12px; }
  .title .line-insight { margin-left: 14px; letter-spacing: 1px; }
  .idea-art {
    position: absolute;
    left: 418px;
    top: 89px;
    width: 226px;
    height: 355px;
    border-radius: 6px;
    background: linear-gradient(180deg, #1f7fa6 0%, #16607f 100%);
  }
  .subtitle {
    position: absolute;
    left: 78px;
    top: 684px;
    margin: 0;
    font-weight: 300;
    font-size: 30.5px;
    letter-spacing: 0.3px;
    color: var(--teal);
    white-space: nowrap;
  }
  .includes-label {
    position: absolute;
    left: 78px;
    top: 752px;
    margin: 0;
    font-family: "Montserrat", Arial, sans-serif;
    font-weight: 600;
    font-size: 18px;
    letter-spacing: 10px;
    color: var(--white);
  }
  .includes-list {
    position: absolute;
    left: 78px;
    top: 786px;
    margin: 0;
    padding: 0;
    list-style: none;
    font-size: 17.5px;
    line-height: 28px;
    letter-spacing: 0.4px;
  }
  .includes-list li { margin-bottom: 28px; }
  .footer-band {
    position: absolute;
    left: 0;
    top: 1020px;
    width: 555px;
    height: 180px;
    background: var(--teal);
  }
  .brand-panel {
    position: absolute;
    left: 555px;
    top: 1020px;
    width: 245px;
    height: 180px;
    background: var(--mist);
  }
  .brand-name {
    position: absolute;
    left: 38px;
    top: 52px;
    display: flex;
    align-items: center;
    gap: 8px;
    font-size: 21px;
    font-weight: 500;
    line-height: 23px;
    color: var(--navy);
  }
  .brand-mark {
    width: 14px;
    height: 14px;
    background: var(--navy);
    flex: none;
  }
  .brand-tagline {
    position: absolute;
    left: 38px;
    top: 142px;
    font-size: 10px;
    letter-spacing: 1.3px;
    color: var(--grey);
  }
</style>
</head>
<body>
  <main class="cover">
    <h1 class="title">
      <span class="line-the">The</span>
      <span class="line-cfo">CFO</span>
      <span class="line-insight">Insight</span>
    </h1>

    <div class="idea-art" role="img" aria-label="Illustration: light bulb formed by a network of connected technology icons"></div>

    <p class="subtitle">The Leading role of CFO in business transformation</p>

    <h2 class="includes-label">INCLUDES</h2>
    <ul class="includes-list">
      <li>Insight into external, enterprise and departmental challenges</li>
      <li>Best practices and strategies to solve these challenges,<br>with a focus on innovation, securing competitive advantage and<br>opportunities for growth</li>
      <li>Finance industry trends in the 2020s</li>
    </ul>

    <div class="footer-band"></div>
    <div class="brand-panel">
      <div class="brand-name"><span class="brand-mark"></span><span>Norvane<br>Document Solutions</span></div>
      <div class="brand-tagline">A HALDEN GROUP COMPANY</div>
    </div>
  </main>
</body>
</html>
```